Colette Vrenick First Time Home Buyer Specialist and Real Estate Matchmaker- fun postcard design

I specialize in first time home buyers in the real estate market. I'm looking for a fun, inviting and memorable postcard. I'd like it to communicate warmth and approachability using different shades of one color with white. it could be pink but it could be another color. I just want it to be bright and fun.
So some background... Being 26 and unmarried in a small jewish community everyone wants to set me up on a date, but they never ask me what I want. In my postcard I want to relay that searching for a home is like dating. Every other realtor is thinking 4 bedroom, 2 bath, colonial, perfect. Similar to the "okay, he's a boy you're a girl, perfect" train of thought. But working with me, I'll be there to take it a step further and listen and hone in on finding what you're LOOKING for. I'm here to prevent the "disaster dates" and show you realistic and charming prospects. It's about the future and building a relationship; not just in love, but in finding your home.
If you can add cute images and slogans like, "let me unite you with the home you've always wanted." (i don't love that one and I'm open to suggestions)
"I want to know exactly what you're looking for"
"True love is the soul's recognition of its counterpoint in another"

I'd like to have my picture featured on the card.

Looking forward to seeing what you come up with. thanks.

Target Market(s)

Real Estate, Students, Young professionals,Newlyweds, First time home buyers, first time renters, young couples, young singles, People looking to sell their homes. Vacation homes and rentals.

Industry/Entity Type

Real Estate

Font styles to use
Serif
Decorative
Script

Requirements
Must have
• Must be easy to read, not too wordy but gets the point across. must have a fun and cute vibe. must have my picture and my Broker's name small at the bottom Sunward Nest Realty. I will attach their logo.
• My contact information.
• Colette Vrenick
• First Time Home Buyer Specialist
• Sunward Nests Realty
• 72 E Orchard Ln
• Tolbury, NJ 07419
• Office: 732-517-2084
• Cell: 732-463-7129
• Cvrenick.sunwardnestsus.example
• Cvrenick@sunwardnestsus.example
Nice to have
• I would like the postcard to have some more pictures besides my own. Either a scenic view of some sort, a lake house, ocean view, maybe people in the picture. Or could just be some nice design. I'm not too picky. Also some added quotes or sayings that apply to my demographic that a designer might know or suggest.
Should not have
• I'm pretty open to wherever the creative process takes you but It just must be uplifting, fun, and inspiring.

```html
<!DOCTYPE html>
<html lang="en">
<head>
<meta charset="utf-8">
<title>Colette Vrenick – First Time Home Buyer Postcard</title>
<link href="https://fonts.googleapis.com/css2?family=Libre+Baskerville:wght@700&family=Lato:wght@400&display=swap" rel="stylesheet">
<style>
  :root {
    --navy: #1e3f7a;
    --red: #e21f3b;
    --white: #ffffff;
    --paper: #f3f3f3;
    --paper-shade: #dcdcdc;
    --stage: #e9e6e2;
    --sky: #a9c4e0;
    --house: #9aa0a8;
    --warm: #e8c98f;
    --grass: #4f7a2e;
    --portrait: #c9a58a;
  }
  * { margin: 0; padding: 0; box-sizing: border-box; }
  html, body { width: 1200px; height: 900px; overflow: hidden; background: var(--stage); }
  .postcard {
    position: absolute; left: 104px; top: 67px;
    width: 992px; height: 765px;
    background: linear-gradient(180deg, var(--white) 0%, var(--paper) 60%, var(--paper-shade) 100%);
    box-shadow: 0 6px 18px rgba(0,0,0,.25);
    overflow: hidden;
  }
  .postcard__shapes { position: absolute; inset: 0; }
  .headline {
    position: absolute; left: 0; right: 0; top: 62px;
    text-align: center;
    font-family: "Libre Baskerville", Georgia, serif; font-weight: 700;
  }
  .headline__lead { display: block; color: var(--navy); font-size: 45px; letter-spacing: .5px; line-height: 54px; }
  .headline__tail { display: block; color: var(--red); font-size: 37px; line-height: 44px; }
  .quote {
    position: absolute; left: 34px; top: 290px; width: 500px;
    color: var(--white);
    font-family: "Libre Baskerville", Georgia, serif; font-weight: 700;
    font-size: 22px; line-height: 30px;
  }
  .agent {
    position: absolute; left: 33px; top: 398px;
    list-style: none; color: var(--white);
    font-family: "Lato", Arial, sans-serif;
  }
  .agent__line { font-size: 21px; line-height: 27px; }
  .agent__contact { font-size: 16px; line-height: 23px; }
  .agent__contact:first-of-type { margin-top: 0; }
  .agent__gap { height: 6px; }
  .broker-mark {
    position: absolute; left: 40px; top: 650px;
    display: flex; align-items: center; gap: 14px;
    color: var(--navy); white-space: nowrap;
    font-family: "Libre Baskerville", Georgia, serif; font-weight: 700;
    font-size: 23px; line-height: 30px; letter-spacing: .5px;
  }
  .broker-mark__square { width: 28px; height: 28px; background: var(--red); flex: none; }
</style>
</head>
<body>
<main class="postcard">
  <svg class="postcard__shapes" viewBox="0 0 992 765" width="992" height="765">
    <defs>
      <linearGradient id="photoTones" x1="0" y1="0" x2="0" y2="1">
        <stop offset="0" stop-color="#a9c4e0"/>
        <stop offset="0.35" stop-color="#9aa0a8"/>
        <stop offset="0.6" stop-color="#e8c98f"/>
        <stop offset="0.8" stop-color="#4f7a2e"/>
        <stop offset="1" stop-color="#3a5b22"/>
      </linearGradient>
    </defs>
    <path class="ribbon-red" d="M0,178 Q300,235 620,250 L600,268 Q300,255 0,215 Z" fill="#e21f3b"/>
    <polygon class="hero-photo" role="img" aria-label="Photo of a smiling young couple sitting on the lawn in front of a large lit suburban house at dusk"
      points="540,240 992,175 992,735 420,735 492,385 532,268" fill="url(#photoTones)"/>
    <path class="sweep-navy" d="M0,160 Q470,300 992,140 L992,168 Q470,325 0,182 Z" fill="#1e3f7a"/>
    <path class="sweep-white" d="M0,182 Q470,325 992,168 L992,180 Q470,338 0,192 Z" fill="#ffffff"/>
    <polygon class="panel-quote" points="7,262 550,262 530,325 500,385 7,385" fill="#e21f3b"/>
    <polygon class="panel-contact" points="7,385 500,385 472,600 7,600" fill="#1e3f7a"/>
    <circle class="agent-portrait" role="img" aria-label="Portrait photo of Colette Vrenick" cx="880" cy="320" r="72" fill="#c9a58a" stroke="#ffffff" stroke-width="6"/>
    <rect class="band-bottom" x="0" y="738" width="992" height="20" fill="#1e3f7a"/>
  </svg>

  <h1 class="headline">
    <span class="headline__lead">LET ME UNITE YOU WITH THE</span>
    <span class="headline__tail">home you've always wanted</span>
  </h1>

  <p class="quote">True love is the soul's recognition<br>of its counterpoint in another</p>

  <ul class="agent">
    <li class="agent__line">Colette Vrenick</li>
    <li class="agent__line">First Time Home Buyer Specialist</li>
    <li class="agent__line">Sunward Nests Realty</li>
    <li class="agent__line">72 E Orchard Ln&nbsp; Tolbury, NJ 07419</li>
    <li class="agent__gap" aria-hidden="true"></li>
    <li class="agent__contact">Office: 732-517-2084&nbsp;&nbsp;·&nbsp;&nbsp;Cell: 732-463-7129</li>
    <li class="agent__contact">Cvrenick@sunwardnestsus.example</li>
    <li class="agent__contact">Cvrenick.sunwardnestsus.example</li>
  </ul>

  <div class="broker-mark">
    <span class="broker-mark__square"></span>
    <span class="broker-mark__name">SUNWARD NESTS REALTY</span>
  </div>
</main>
</body>
</html>
```